Mistholm Consulting Business

** Please add the content information from my old business card
1. I would like to see a two sided business card with both options with the 1st Option--Sketch Forge-new WHITE BACKGROUND LOGO
2 nd Option-Sketch Forge - new BLACK- Background Logo
3rd -Option a business card with my Photo on the card
Please add the new word to the card information:
EXECUTION
AS THE OWNER'S REP
WE AIM TO ACHIEVE YOUR
INFRASTRUCTURE VISION with
OUR SPECIALIZATION & EXECUTION in:

FUNDING Planning
BUSINESS Planning
INFRASTRUCTURE Planning
PROJECT Management
Since 2012
_____________________________________________________________________
I want to get spot uv raised printing. I was liking a a nice rich white linen paper stock with black writing & NOT A COLORED CARD other than a variety of white or black cards concept

```html
<!DOCTYPE html>
<html lang="en">
<head>
<meta charset="utf-8">
<title>Mistholm Consulting – Business Card</title>
<link href="https://fonts.googleapis.com/css2?family=Lato:wght@400;700;900&display=swap" rel="stylesheet">
<style>
  :root{
    --backdrop:#2b2b2d;
    --card:#262628;
    --card-edge:#1c1c1e;
    --ink:#f2f2f2;
    --ink-soft:#cfcfcf;
    --gloss:#9a9a9c;
    --accent:#e5173a;
  }
  *{margin:0;padding:0;box-sizing:border-box}
  html,body{width:1200px;height:799px;overflow:hidden;background:var(--backdrop);font-family:"Lato",sans-serif}
  .canvas{position:relative;width:1200px;height:799px}
  .card{position:absolute;width:540px;height:308px;background:var(--card);border:1px solid var(--card-edge);box-shadow:0 18px 40px rgba(0,0,0,.45);overflow:hidden}
  .card--back{left:50px;top:90px}
  .card--front{left:610px;top:400px}

  /* brand name set as plain text */
  .brand{display:flex;align-items:center;gap:10px;color:var(--gloss);font-weight:900;letter-spacing:.5px;line-height:1}
  .brand__mark{width:12px;height:12px;background:var(--accent)}

  /* back side */
  .card--back .brand{position:absolute;left:36px;bottom:48px;font-size:40px}
  .pitch{position:absolute;left:280px;top:44px;color:var(--ink);font-size:12.5px;font-weight:900;line-height:1.45;letter-spacing:.3px}
  .pitch__rule{width:46px;height:2px;background:var(--accent);margin:10px 0 8px}
  .services{list-style:none;color:var(--ink);font-size:12.5px;line-height:1.45}
  .services b{font-weight:900;letter-spacing:.3px}
  .services span{font-weight:400;color:var(--ink-soft)}
  .since{position:absolute;right:26px;bottom:22px;color:var(--ink-soft);font-size:11px}

  /* front side */
  .card--front .brand{position:absolute;right:34px;top:34px;font-size:40px}
  .person{position:absolute;right:34px;top:112px;text-align:right}
  .person__name{color:var(--ink);font-size:23px;font-weight:900}
  .person__role{color:var(--accent);font-size:12px;letter-spacing:.6px;margin-top:4px}
  .accent-bar{position:absolute;right:0;top:140px;width:9px;height:40px;background:var(--accent)}
  .contact{position:absolute;right:34px;top:186px;list-style:none;text-align:right;color:var(--ink);font-size:13px;line-height:1.55}
  .contact li{display:flex;justify-content:flex-end;align-items:center;gap:10px}
  .contact svg{width:11px;height:11px;fill:var(--accent)}
</style>
</head>
<body>
<main class="canvas">

  <section class="card card--back" aria-label="Card back">
    <div class="brand"><span class="brand__mark"></span>Mistholm</div>
    <div class="pitch">
      <p>EXECUTION<br>AS THE OWNER'S REP<br>WE AIM TO ACHIEVE YOUR<br>INFRASTRUCTURE VISION with<br>OUR SPECIALIZATION &amp; EXECUTION in:</p>
      <div class="pitch__rule"></div>
      <ul class="services">
        <li><b>FUNDING</b> <span>Planning</span></li>
        <li><b>BUSINESS</b> <span>Planning</span></li>
        <li><b>INFRASTRUCTURE</b> <span>Planning</span></li>
        <li><b>PROJECT</b> <span>Management</span></li>
      </ul>
    </div>
    <p class="since">Since 2012</p>
  </section>

  <section class="card card--front" aria-label="Card front">
    <div class="brand"><span class="brand__mark"></span>Mistholm</div>
    <div class="person">
      <p class="person__name">Helena Marsh-Okafor</p>
      <p class="person__role">CEO / LEAD PROJECT MANAGER</p>
    </div>
    <div class="accent-bar"></div>
    <ul class="contact">
      <li>555.010.4821 <svg viewBox="0 0 12 12"><rect x="3" y="0" width="6" height="12" rx="1.2"/></svg></li>
      <li>helena@mistholm.ca <svg viewBox="0 0 12 12"><path d="M0 2h12v8H0zM1 3l5 3.5L11 3z"/></svg></li>
      <li>www.mistholm.ca <svg viewBox="0 0 12 12"><circle cx="6" cy="6" r="6"/></svg></li>
      <li>Northvale NT <svg viewBox="0 0 12 12"><path d="M6 0a4 4 0 0 1 4 4c0 3-4 8-4 8S2 7 2 4a4 4 0 0 1 4-4z"/></svg></li>
      <li>Eastbrook NB <svg viewBox="0 0 12 12"><path d="M6 0a4 4 0 0 1 4 4c0 3-4 8-4 8S2 7 2 4a4 4 0 0 1 4-4z"/></svg></li>
    </ul>
  </section>

</main>
</body>
</html>
```